App Design for Restaurant App

We need a design for the new Mobile App for the Restaurant Volmik. See attachment for presentation sketches.
There are two attached files: File 2 shows the App in general and File 1 shows the five screens which need to be designed. Your work should contain the general color scheme, icons and layout proposal.
Updates
Hi Designers
There where several questions about the scope of the work. We are looking for a design for an App. The promotion website of the restaurant Volmik can be found under www.restaurant-volmik.ch
There you will get an impression of the Corporate Identity used by the restaurant and you will also find the logo.
In the sketch there are several screens which don't need a design, e.g. the cover flow or video screen
please ask if you have any question
kind regards
Tobias
Industry/Entity Type
Restaurant
Look and feel
Each slider illustrates characteristics of the customer's brand and the style your logo design should communicate.

```html
<!DOCTYPE html>
<html lang="de">
<head>
<meta charset="utf-8">
<title>Restaurant Volmik – Kontakt</title>
<link rel="stylesheet" href="https://fonts.googleapis.com/css2?family=Source+Sans+3:wght@400;500&display=swap">
<style>
  :root {
    --canvas: #ffffff;
    --cream: #f8f6c6;
    --olive: #434c1c;
    --olive-dark: #3a4217;
    --card: #ffffff;
    --frame: #1a1a1a;
    --photo-light: #e9e4d8;
    --photo-mid: #c9b79a;
    --photo-dark: #8a6a45;
  }
  * { margin: 0; padding: 0; box-sizing: border-box; }
  html, body {
    width: 1200px; height: 900px; overflow: hidden;
    background: var(--canvas);
    font-family: "Source Sans 3", "Myriad Pro", sans-serif;
    color: var(--olive);
  }
  .screen {
    position: absolute; left: 80px; top: 78px;
    width: 487px; height: 729px;
    background: var(--cream);
    border: 1px solid var(--frame);
  }
  .header {
    position: absolute; left: 48px; top: 19px;
    width: 392px; height: 121px;
    background: var(--card);
  }
  .brand-name {
    position: absolute; left: 0; right: 14px; top: 86px;
    text-align: center;
    font-size: 30px; font-weight: 400; letter-spacing: 0.2px;
    color: var(--olive);
    line-height: 1;
  }
  .back-button {
    position: absolute; left: -3px; top: 45px;
    width: 102px; height: 39px;
  }
  .back-button span {
    position: absolute; left: 29px; top: 8px;
    color: #fff; font-size: 20px; line-height: 1;
  }
  .menu-icon {
    position: absolute; left: 336px; top: 36px;
    width: 49px; height: 48px;
  }
  .hero-photo {
    position: absolute; left: 16px; top: 160px;
    width: 454px; height: 147px;
    background: var(--card);
    padding: 9px 1px 8px 2px;
  }
  .hero-photo div {
    width: 100%; height: 100%;
    background: linear-gradient(180deg, var(--photo-light) 0%, #f1ede4 45%, var(--photo-mid) 75%, var(--photo-dark) 100%);
  }
  .panel {
    position: absolute; left: 49px;
    width: 391px;
    background: var(--card);
    box-shadow: 6px 6px 0 var(--olive-dark);
  }
  .panel-title {
    top: 317px; height: 55px;
    text-align: center;
    font-size: 30px; font-weight: 400; line-height: 57px;
  }
  .contact-info {
    top: 392px; height: 280px;
    padding: 12px 0 0 19px;
    font-size: 19.5px; line-height: 25.5px;
  }
  .contact-info p + p { margin-top: 25.5px; }
</style>
</head>
<body>
  <main class="screen">
    <header class="header">
      <div class="brand-name">RESTAURANT VOLMIK</div>
      <svg class="menu-icon" viewBox="0 0 49 48" aria-label="Menü">
        <rect x="0" y="0" width="21" height="20" fill="var(--olive)"/>
        <rect x="28" y="0" width="21" height="20" fill="var(--olive)"/>
        <rect x="0" y="27" width="21" height="21" fill="var(--olive)"/>
        <rect x="28" y="27" width="21" height="21" fill="var(--olive)"/>
      </svg>
    </header>

    <a class="back-button" aria-label="Zurück">
      <svg width="102" height="39" viewBox="0 0 102 39">
        <path d="M14 1 H101 V38 H14 L1 22 Q0 19.5 1 17 Z" fill="var(--olive)" stroke="#2e3410" stroke-width="1"/>
      </svg>
      <span>Zurück</span>
    </a>

    <figure class="hero-photo"><div role="img" aria-label="Festlich gedeckter Speisesaal mit weissen Tischen und Panoramafenstern"></div></figure>

    <h1 class="panel panel-title">KONTAKT</h1>

    <section class="panel contact-info">
      <p>info@restaurant-volmik.ch<br>Restaurant Volmik<br>Volmikstrasse<br>6300 Talhausen/ZG</p>
      <p>T: +41 (0)41 555 01 20<br>F: +41 (0)41 555 01 21</p>
      <p>Öffnungszeiten<br>Täglich geöffnet</p>
    </section>
  </main>
</body>
</html>
```